New Billboard Design Project

I would like to have a banner made which is approx 16ft wide x 8ft tall showing our 3 businesses. I would like to use the new Vellmor Yard Supply Logo as the main , and have them all incorporated in one banner. I would like to have a nice background that would go with construction, excavation and material supply yard which sells landscape materials,
Updates

Low design quality

Adding photos to be incorporated

Target Market(s)

contractors, homeowners, landscapers, developers

Industry/Entity Type

Construction, land clearing, concrete foundations, Excaavation

Requirements
Must have
• excavation, concrete, all three logos

```html
<!DOCTYPE html>
<html lang="en">
<head>
<meta charset="utf-8">
<title>Vellmor Yard Supply – Billboard</title>
<link href="https://fonts.googleapis.com/css2?family=Anton&display=swap" rel="stylesheet">
<style>
  :root {
    --brown: #6e2a2a;
    --green: #1f9a48;
    --maroon: #7a1f3a;
    --red: #e32026;
    --charcoal: #4a4747;
    --white: #ffffff;
    --sky: #3f86cc;
    --cloud: #e6edf4;
    --machine: #f39a2a;
    --soil: #7e5236;
  }
  html, body { margin: 0; padding: 0; overflow: hidden; background: var(--white); }
  .billboard {
    position: relative;
    width: 1200px;
    height: 600px;
    overflow: hidden;
    background: var(--white);
    font-family: "Anton", "Arial Narrow", sans-serif;
  }
  .hero-art { position: absolute; inset: 0; width: 1200px; height: 600px; }

  .brand-main {
    position: absolute;
    left: 42px; top: 44px;
    display: flex; align-items: center; gap: 20px;
  }
  .brand-main .dot {
    width: 96px; height: 96px; border-radius: 50%;
    background: var(--green); flex: none;
  }
  .brand-main .name {
    margin: 0;
    font-weight: 400;
    color: var(--brown);
    font-size: 66px; line-height: 1;
    letter-spacing: 1px;
    text-transform: uppercase;
  }

  .partner {
    position: absolute;
    text-transform: uppercase;
    line-height: 1.05;
    font-weight: 400;
  }
  .partner .sub { display: block; }
  .partner--homes {
    left: 54px; top: 276px;
    color: var(--maroon);
    font-size: 40px;
  }
  .partner--homes .sub { font-size: 22px; letter-spacing: 2.4px; }
  .partner--excavation {
    left: 345px; top: 276px;
    color: var(--red);
    font-size: 40px;
  }
  .partner--excavation .sub { font-size: 22px; letter-spacing: 1.6px; }

  .contact {
    position: absolute;
    left: 38px; top: 400px;
    display: flex; align-items: center; gap: 32px;
  }
  .contact svg { width: 56px; height: 56px; flex: none; }
  .contact .phone {
    color: var(--red);
    font-size: 94px; line-height: 1;
    letter-spacing: 1px;
  }

  .services {
    position: absolute;
    left: 0; top: 510px;
    width: 1200px; height: 72px;
    background: var(--red);
    margin: 0; padding: 0; list-style: none;
  }
  .services li {
    position: absolute;
    top: 13px;
    color: var(--white);
    font-size: 45px; line-height: 1;
    text-transform: uppercase;
    display: flex; align-items: center; gap: 22px;
  }
  .services li::before {
    content: ""; width: 16px; height: 16px; border-radius: 50%;
    background: var(--white);
  }
  .services .item-construction { left: 50px; }
  .services .item-excavation { left: 396px; }
  .services .item-supply { left: 686px; }
</style>
</head>
<body>
<main class="billboard">
  <svg class="hero-art" viewBox="0 0 1200 600">
    <defs>
      <linearGradient id="siteGradient" x1="0" y1="0" x2="0.35" y2="1">
        <stop offset="0" stop-color="var(--sky)"/>
        <stop offset="0.3" stop-color="var(--cloud)"/>
        <stop offset="0.5" stop-color="var(--machine)"/>
        <stop offset="0.72" stop-color="#a26d47"/>
        <stop offset="1" stop-color="var(--soil)"/>
      </linearGradient>
    </defs>
    <polygon class="chevron" fill="var(--charcoal)"
      points="600,0 620,0 563,108 678,340 671,340 533,108"/>
    <g role="img" aria-label="Photo of an orange excavator digging a pile of soil under a blue cloudy sky">
      <polygon fill="url(#siteGradient)"
        points="626,0 1200,0 1200,475 838,475 768,340 687,340 572,108"/>
    </g>
    <g class="stripes" fill="var(--charcoal)">
      <polygon points="671,345 699,345 741,433 713,433"/>
      <polygon points="708,345 736,345 778,433 750,433"/>
      <polygon points="745,345 768,345 808,430 786,430"/>
    </g>
  </svg>

  <header class="brand-main">
    <span class="dot"></span>
    <h1 class="name">Vellmor Yard<br>Supply</h1>
  </header>

  <div class="partner partner--homes">Brenwick Homes<span class="sub">Construction Co.</span></div>
  <div class="partner partner--excavation">Darrow<span class="sub">Excavation Co.</span></div>

  <div class="contact">
    <svg viewBox="0 0 24 24" aria-hidden="true">
      <path fill="var(--red)" d="M6.6 10.8a15.1 15.1 0 0 0 6.6 6.6l2.2-2.2a1 1 0 0 1 1-.25 11.4 11.4 0 0 0 3.6.57 1 1 0 0 1 1 1V20a1 1 0 0 1-1 1A17 17 0 0 1 3 4a1 1 0 0 1 1-1h3.5a1 1 0 0 1 1 1c0 1.25.2 2.450.57 3.57a1 1 0 0 1-.25 1z"/>
      <path fill="none" stroke="var(--red)" stroke-width="1.6" stroke-linecap="round" d="M14 3.5a7 7 0 0 1 6.5 6.5M14 7a3.5 3.5 0 0 1 3 3"/>
    </svg>
    <span class="phone">0198 765 432</span>
  </div>

  <ul class="services">
    <li class="item-construction">Construction</li>
    <li class="item-excavation">Excavation</li>
    <li class="item-supply">Material Supply Yard</li>
  </ul>
</main>
</body>
</html>
```